Visitenkarten-Design für Garten- und Landschaftspflege
Tamuga Vent setzte meine Vorstellungen absolut super um ich kann Ihn nur weiter empfehlen. vielen dank
Zielgruppe
Baumpflege, Baumfällung, Garten und Landschaftspflege meine zielgruppe sind Privatpersonen im alter von 20-100Jahren
Aufgabenstellung
Sehr geehrte Damen und Herren, die visitenkarte sollte die angaben so enthalten wie sie auf der von mir gestallteten Visitenkarten sind ( meine ist kein maß der Dinge). Ich habe mein Logo leider nur als 3.jpg Datei. Das Logo darf im Design erändert werden aber bitte nur Feinheiten ansonsten stehen ihnen alle türen offen um kreativ zu sein.
mit freundlichen Grüßen Holger Banzow

```html
<!DOCTYPE html>
<html lang="de">
<head>
<meta charset="utf-8">
<title>Visitenkarte Baumpflege Banzow</title>
<link href="https://fonts.googleapis.com/css2?family=Lato:wght@300;400;700;900&display=swap" rel="stylesheet">
<style>
  :root {
    --page: #f4f4f2;
    --cream: #efebe0;
    --cream-back: #ebe6d6;
    --bark: #6b6762;
    --tree-faint: #ddd4ba;
    --accent: #d46a48;
    --ink: #1e1c1a;
    --muted: #7a7670;
  }
  * { box-sizing: border-box; margin: 0; padding: 0; }
  html, body { width: 1200px; height: 1200px; overflow: hidden; }
  body {
    background: var(--page);
    font-family: "Lato", sans-serif;
    position: relative;
  }
  .card {
    position: absolute;
    top: 258px;
    width: 440px;
    height: 684px;
    overflow: hidden;
  }
  .card-front { left: 130px; background: var(--cream); }
  .card-back { left: 630px; background: var(--cream-back); }

  .art { position: absolute; inset: 0; width: 100%; height: 100%; }

  .wordmark {
    position: absolute;
    top: 44px;
    left: 0;
    width: 100%;
    text-align: center;
    color: var(--accent);
    font-weight: 900;
    font-size: 54px;
    line-height: 1.02;
    letter-spacing: 1px;
  }

  .contact {
    position: absolute;
    left: 215px;
    top: 478px;
    color: var(--muted);
    font-weight: 300;
    font-size: 15px;
    line-height: 20px;
  }
  .contact .name {
    color: var(--accent);
    font-weight: 400;
    font-size: 21px;
    line-height: 28px;
    margin-bottom: 2px;
  }

  .services-title {
    position: absolute;
    left: 32px;
    top: 164px;
    color: var(--accent);
    font-size: 20px;
    letter-spacing: 2px;
    font-weight: 400;
  }
  .services {
    position: absolute;
    left: 32px;
    top: 224px;
    list-style: none;
    color: var(--ink);
    font-size: 15px;
  }
  .services li {
    display: flex;
    align-items: center;
    height: 34px;
  }
  .services svg { width: 22px; height: 16px; margin-right: 8px; flex: none; }
  .services small { font-size: 12.5px; }
  .tagline {
    position: absolute;
    left: 32px;
    top: 592px;
    color: var(--accent);
    font-size: 20px;
    line-height: 27px;
    letter-spacing: 2px;
  }
</style>
</head>
<body>

<section class="card card-front">
  <svg class="art" viewBox="0 0 440 684" role="img" aria-label="Illustration: dunkle Baumkrone mit Stamm, Kolibri und Libelle">
    <defs>
      <linearGradient id="canopy" x1="0" y1="0" x2="0" y2="1">
        <stop offset="0" stop-color="#6b6762"/>
        <stop offset="0.42" stop-color="#6b6762"/>
        <stop offset="0.62" stop-color="#efebe0"/>
      </linearGradient>
    </defs>
    <rect width="440" height="684" fill="url(#canopy)"/>
  </svg>
  <div class="wordmark">BAUMPFLEGE<br>BANZOW</div>
  <div class="contact">
    <p class="name">HOLGER BANZOW</p>
    <p>Fachagrarwirt Baumpflege/</p>
    <p>Baumsanierung</p>
    <p>Lindenweg 7</p>
    <p>85599 Ahornfeld</p>
    <p>0170 12 34 567</p>
    <p>kontakt@baumpflege-banzow.de</p>
  </div>
</section>

<section class="card card-back">
  <svg class="art" viewBox="0 0 440 684" role="img" aria-label="Illustration: blasse Baumsilhouette im Hintergrund">
    <defs>
      <linearGradient id="faint" x1="0" y1="0" x2="0" y2="1">
        <stop offset="0" stop-color="#ddd4ba"/>
        <stop offset="0.5" stop-color="#e4ddc7"/>
        <stop offset="1" stop-color="#ebe6d6"/>
      </linearGradient>
    </defs>
    <rect width="440" height="684" fill="url(#faint)"/>
  </svg>
  <h2 class="services-title">UNSERE LEISTUNGEN</h2>
  <ul class="services">
    <li><svg viewBox="0 0 22 16"><path d="M1 6h11V1l9 7-9 7V10H1z" fill="var(--accent)"/></svg>Neue Pflanzungen</li>
    <li><svg viewBox="0 0 22 16"><path d="M1 6h11V1l9 7-9 7V10H1z" fill="var(--accent)"/></svg>Herstellen der Verkehrssicherheit von Baumen</li>
    <li><svg viewBox="0 0 22 16"><path d="M1 6h11V1l9 7-9 7V10H1z" fill="var(--accent)"/></svg>Kronenrückschnitt&nbsp;<small>(Einkürzungen und Kronenpflege)</small></li>
    <li><svg viewBox="0 0 22 16"><path d="M1 6h11V1l9 7-9 7V10H1z" fill="var(--accent)"/></svg>Prüfen von Bäumen auf Standsicherheit</li>
    <li><svg viewBox="0 0 22 16"><path d="M1 6h11V1l9 7-9 7V10H1z" fill="var(--accent)"/></svg>Fällung von Bäumen</li>
    <li><svg viewBox="0 0 22 16"><path d="M1 6h11V1l9 7-9 7V10H1z" fill="var(--accent)"/></svg>Obstbaumschnitt</li>
    <li><svg viewBox="0 0 22 16"><path d="M1 6h11V1l9 7-9 7V10H1z" fill="var(--accent)"/></svg>Fräsen von Wurzelstöcken</li>
  </ul>
  <p class="tagline">AUFBAU UND ANFERTIGUNG VON<br>GARTENHÄUSERN NACH MAß.</p>
</section>

</body>
</html>
```